Business Card Design

We would like a business card that utilizes our current logo and keeps with the same feel - elegant and organic. Our farm isn't about mass production, it's about excellence, education, beautiful events and flowers - people, culture, and community.

Target Market(s)

Patrons to our farm who are interested in weddings, events, or our flowers and vegetables.

Contact Information for Business Card

Name, address, cell email (Danielle Hoskins, 2716 Wrenfield Rd, Ashby Falls, CO 80619, cell 30.412.6638, email danielle@wrenfieldacres.com)

```html
<!DOCTYPE html>
<html lang="en">
<head>
<meta charset="utf-8">
<title>Wrenfield Acres – Business Card</title>
<link rel="stylesheet" href="https://fonts.googleapis.com/css2?family=Roboto:wght@400;500&display=swap">
<style>
  :root {
    --backdrop: #2c2c2c;
    --paper: #ffffff;
    --sage: #768a79;
    --tan: #a7815b;
    --ink: #2f2f2f;
    --white: #ffffff;
  }
  * { box-sizing: border-box; margin: 0; padding: 0; }
  html, body {
    width: 1200px; height: 1200px; overflow: hidden;
    background: var(--backdrop);
    font-family: "Roboto", sans-serif;
  }
  .card {
    position: absolute; left: 235px; width: 730px; height: 416px;
    box-shadow: 0 4px 10px rgba(0,0,0,.55);
  }
  .card--front { top: 160px; background: var(--paper); }
  .card--back { top: 625px; background: var(--tan); }

  .brand {
    position: absolute; left: 0; right: 0;
    display: flex; align-items: center; justify-content: center; gap: 12px;
    font-weight: 400; letter-spacing: 4px; text-transform: uppercase;
  }
  .brand__dot { width: 14px; height: 14px; border-radius: 50%; }
  .card--front .brand { top: 100px; font-size: 34px; color: var(--sage); }
  .card--front .brand__dot { background: var(--sage); }
  .card--back .brand { top: 178px; font-size: 40px; color: var(--white); }
  .card--back .brand__dot { background: var(--white); }

  .person {
    position: absolute; right: 398px; top: 254px; text-align: right;
  }
  .person__name { font-size: 25px; font-weight: 500; color: var(--sage); line-height: 1.1; }
  .person__title { font-size: 18px; color: var(--ink); margin-top: 6px; }

  .divider {
    position: absolute; left: 350px; top: 235px; width: 2px; height: 93px; background: var(--ink);
  }

  .contact { position: absolute; left: 368px; top: 238px; list-style: none; }
  .contact__item {
    display: flex; align-items: center; gap: 10px;
    font-size: 18px; color: var(--ink); height: 28px;
  }
  .contact__icon { width: 13px; height: 13px; fill: var(--tan); flex: none; }

  .address-band {
    position: absolute; left: 0; right: 0; top: 354px; height: 32px;
    background: var(--sage); color: var(--white);
    font-size: 17px; display: flex; align-items: center; justify-content: center;
  }

  .website {
    position: absolute; left: 0; right: 0; top: 351px; text-align: center;
    font-size: 17px; color: var(--white); letter-spacing: 1.5px;
  }
</style>
</head>
<body>
  <section class="card card--front">
    <div class="brand"><span class="brand__dot"></span>Wrenfield Acres</div>

    <div class="person">
      <p class="person__name">DANIELLE HOSKINS</p>
      <p class="person__title">Founder and CEO</p>
    </div>

    <div class="divider"></div>

    <ul class="contact">
      <li class="contact__item">
        <svg class="contact__icon" viewBox="0 0 24 24"><path d="M6.6 10.8a15.1 15.1 0 0 0 6.6 6.6l2.2-2.2a1 1 0 0 1 1-.25 11.4 11.4 0 0 0 3.6.57 1 1 0 0 1 1 1V20a1 1 0 0 1-1 1A17 17 0 0 1 3 4a1 1 0 0 1 1-1h3.5a1 1 0 0 1 1 1c0 1.250.2 2.45.57 3.57a1 1 0 0 1-.25 1z"/></svg>
        030.412.6638
      </li>
      <li class="contact__item">
        <svg class="contact__icon" viewBox="0 0 24 24"><path d="M2 5h20v2l-10 6L2 7z"/><path d="M2 9l10 6 10-6v10H2z"/></svg>
        danielle@wrenfieldacres.com
      </li>
      <li class="contact__item">
        <svg class="contact__icon" viewBox="0 0 24 24"><path d="M12 2a10 10 0 1 0 0 20 10 10 0 0 0 0-20zm0 2c.9 1.1 1.7 2.8 2 5h-4c.3-2.2 1.1-3.9 2-5zM4.3 9h3.7c-.1.7-.1 1.3-.1 2v1H4.1a8 8 0 0 1 .2-3zm.6 6h3.3c.3 1.8.8 3.3 1.5 4.4A8 8 0 0 1 4.9 15zM10 15h4c-.3 2-1.1 3.8-2 5-.9-1.2-1.7-3-2-5zm0-2v-2c0-.7 0-1.3.1-2h3.8c.1.7.1 1.3.1 2v2zm5.8 2h3.3a8 8 0 0 1-4.8 4.4c.7-1.1 1.2-2.6 1.5-4.4zm.2-2v-1c0-.7 0-1.3-.1-2h3.8a8 8 0 0 1 .2 3z"/></svg>
        wrenfieldacres.com
      </li>
    </ul>

    <div class="address-band">2716 Wrenfield Rd, Ashby Falls, CO 80619</div>
  </section>

  <section class="card card--back">
    <div class="brand"><span class="brand__dot"></span>Wrenfield Acres</div>
    <p class="website">www.wrenfieldacres.com</p>
  </section>
</body>
</html>
```